Metal can design

Dear Tormevka
i have already product with plastic bottle , i want to convert it to metal can with more creative design but its design inspired by the old plastic bottle design ...
you can change the color and add piston if you see its better
i want design for
20W50 1L Cylindrical as attached pictures and 4 and 5L rectangular
10W30 Rectangular for 4 and 5L
5W30 Rectangular for 4L Only

i will attached many pictures you inspired idea from it

```html
<!DOCTYPE html>
<html lang="en">
<head>
<meta charset="utf-8">
<title>Vorten Lubricants 20W50 – Metal Can Labels</title>
<link rel="stylesheet" href="https://fonts.googleapis.com/css2?family=Anton&family=Oswald:wght@600;700&family=Roboto:wght@400;700;900&family=Hind:wght@500&display=swap">
<style>
  :root {
    --paper-left: #f6f4f0;
    --paper-right: #ffffff;
    --label: #ffffff;
    --label-edge: #e3e3e6;
    --brand-blue: #1a4fa8;
    --numeral-blue: #1565b4;
    --band-blue: #1a5cb0;
    --band-red: #8e1420;
    --volume-red: #a3121e;
    --ink: #2a2a2a;
    --gold: #c9a23a;
    --gold-dark: #9a7424;
    --badge-dark: #1b1b22;
  }
  * { box-sizing: border-box; margin: 0; padding: 0; }
  html, body { width: 1200px; height: 909px; overflow: hidden; }
  body {
    position: relative;
    background: linear-gradient(90deg, var(--paper-left) 0 542px, var(--paper-right) 542px);
    font-family: "Roboto", Arial, sans-serif;
    color: var(--ink);
  }

  /* ---------- label shell ---------- */
  .label {
    position: absolute;
    background: var(--label);
    border: 1px solid var(--label-edge);
    border-radius: 4px;
  }
  .label > * { position: absolute; }
  .label--round { left: 183px; top: 215px; width: 262px; height: 548px; }
  .label--box   { left: 592px; top: 177px; width: 417px; height: 608px; }

  /* ---------- brand ---------- */
  .brand {
    display: flex; align-items: center; gap: 8px;
    border: 2px solid var(--brand-blue);
    border-radius: 10px;
    padding: 0 10px;
  }
  .brand__dot {
    flex: none; border-radius: 50%;
    background: var(--brand-blue);
  }
  .brand__name {
    font-family: "Roboto", Arial, sans-serif;
    font-weight: 900;
    color: var(--brand-blue);
    letter-spacing: 1px;
    line-height: 1;
  }
  .label--round .brand { left: 14px; top: 37px; width: 234px; height: 49px; }
  .label--round .brand__dot { width: 30px; height: 30px; }
  .label--round .brand__name { font-size: 38px; }
  .label--box .brand { left: 47px; top: 38px; width: 320px; height: 64px; }
  .label--box .brand__dot { width: 42px; height: 42px; }
  .label--box .brand__name { font-size: 52px; }

  .range {
    font-family: "Oswald", sans-serif;
    font-weight: 700;
    color: var(--band-red);
    text-align: center;
    letter-spacing: 5px;
    line-height: 1;
  }
  .label--round .range { left: 14px; top: 96px; width: 234px; font-size: 23px; }
  .label--box .range   { left: 47px; top: 108px; width: 320px; font-size: 31px; letter-spacing: 7px; }

  .tagline {
    font-family: "Hind", sans-serif;
    font-weight: 500;
    color: #222;
    white-space: nowrap;
    line-height: 1;
  }
  .label--round .tagline { left: 14px; top: 126px; font-size: 14.5px; }
  .label--box .tagline   { left: 47px; top: 143px; font-size: 19.5px; }

  /* ---------- grade ---------- */
  .grade { overflow: visible; }
  .grade text {
    font-family: "Anton", Impact, sans-serif;
    fill: var(--numeral-blue);
  }
  .label--round .grade { left: 12px; top: 178px; width: 236px; height: 82px; }
  .label--box .grade   { left: 45px; top: 192px; width: 324px; height: 98px; }

  /* ---------- bands ---------- */
  .band {
    font-family: "Anton", Impact, sans-serif;
    font-weight: 400;
    color: #fff;
    line-height: 1;
    white-space: nowrap;
    display: flex; align-items: center;
    padding-left: 8px;
    clip-path: polygon(0 0, 100% 0, 92% 100%, 0 100%);
  }
  .band--red  { background: linear-gradient(90deg, #7a0f18, var(--band-red) 60%, #b01d2a); }
  .band--blue { background: linear-gradient(90deg, #14479a, var(--band-blue) 70%, #2270c4); }
  .label--round .band--red  { left: 13px; top: 275px; width: 222px; height: 27px; font-size: 17px; }
  .label--round .band--blue { left: 13px; top: 364px; width: 146px; height: 20px; font-size: 13px; }
  .label--box .band--red    { left: 45px; top: 303px; width: 307px; height: 33px; font-size: 23px; padding-left: 12px; }
  .label--box .band--blue   { left: 45px; top: 398px; width: 206px; height: 25px; font-size: 17px; padding-left: 10px; }

  .approvals { font-weight: 400; line-height: 1.3; white-space: nowrap; }
  .label--round .approvals { left: 14px; top: 310px; font-size: 11px; }
  .label--box .approvals   { left: 45px; top: 343px; font-size: 13px; line-height: 1.2; }

  .spec { font-weight: 700; line-height: 1.3; white-space: nowrap; }
  .label--round .spec { left: 14px; top: 390px; font-size: 10.5px; }
  .label--box .spec   { left: 45px; top: 428px; font-size: 13px; }

  /* ---------- seal & volume ---------- */
  .seal {
    border-radius: 50%;
    background: radial-gradient(circle, #e2c46a 0 35%, var(--gold) 60%, var(--gold-dark));
  }
  .label--round .seal { left: 168px; top: 395px; width: 66px; height: 70px; }
  .label--box .seal   { left: 259px; top: 403px; width: 98px; height: 100px; }

  .volume {
    font-family: "Roboto", Arial, sans-serif;
    font-weight: 900;
    color: var(--volume-red);
    line-height: 1;
    letter-spacing: 2px;
  }
  .label--round .volume { left: 14px; top: 465px; font-size: 62px; }
  .label--box .volume   { left: 47px; top: 500px; font-size: 74px; letter-spacing: 6px; }

  /* ---------- footer badges ---------- */
  .award { border-radius: 2px; }
  .award--gold { background: linear-gradient(180deg, #d7b45a, var(--gold-dark)); }
  .award--dark { background: var(--badge-dark); }
  .label--round .award--gold { left: 120px; top: 490px; width: 59px; height: 44px; }
  .label--round .award--dark { left: 181px; top: 491px; width: 33px; height: 43px; }
  .label--box .award--gold   { left: 201px; top: 511px; width: 77px; height: 57px; }
  .label--box .award--dark   { left: 282px; top: 511px; width: 50px; height: 57px; }

  .purity {
    background: linear-gradient(180deg, #e6c25e, var(--gold));
    color: #111;
    font-family: "Roboto", Arial, sans-serif;
    font-weight: 900;
    text-align: center;
    line-height: 1.05;
    display: flex; flex-direction: column; justify-content: center;
  }
  .purity__big { display: block; }
  .label--round .purity { left: 217px; top: 492px; width: 27px; height: 42px; font-size: 7px; }
  .label--round .purity__big { font-size: 13px; }
  .label--box .purity { left: 337px; top: 511px; width: 48px; height: 57px; font-size: 10px; }
  .label--box .purity__big { font-size: 20px; }
</style>
</head>
<body>

  <!-- 1 L round can -->
  <section class="label label--round" aria-label="1 litre round can label">
    <div class="brand"><span class="brand__dot"></span><span class="brand__name">VORTEN</span></div>
    <div class="range">LUBRICANTS</div>
    <div class="tagline">High Power Technology Engine Oil</div>
    <svg class="grade" viewBox="0 0 236 82" aria-label="20W50">
      <text x="0" y="80" font-size="90" textLength="236" lengthAdjust="spacingAndGlyphs">20W50</text>
    </svg>
    <div class="band band--red">MEETS THE REQUIREMENTS</div>
    <p class="approvals">KR 229.1, TRX M 271 DTFR<br>15B110, AISON C4 HALVO<br>VDS GRANTEC TO-2</p>
    <div class="band band--blue">SPECIFICATION</div>
    <p class="spec">APX SL/CF,<br>AVEA A3/B4<br>MINERAL OIL</p>
    <div class="seal" role="img" aria-label="Gold grade seal"></div>
    <div class="volume">1L</div>
    <div class="award award--gold" role="img" aria-label="Award badge"></div>
    <div class="award award--dark" role="img" aria-label="Reader award badge"></div>
    <div class="purity">100%<br>VIRGIN<span class="purity__big">OIL</span></div>
  </section>

  <!-- 4 L rectangular can -->
  <section class="label label--box" aria-label="4 litre rectangular can label">
    <div class="brand"><span class="brand__dot"></span><span class="brand__name">VORTEN</span></div>
    <div class="range">LUBRICANTS</div>
    <div class="tagline">High Power Technology Engine Oil</div>
    <svg class="grade" viewBox="0 0 324 98" aria-label="20W50">
      <text x="0" y="96" font-size="108" textLength="324" lengthAdjust="spacingAndGlyphs">20W50</text>
    </svg>
    <div class="band band--red">MEETS THE REQUIREMENTS</div>
    <p class="approvals">KR 229.1, TRX M 271 DTFR<br>15B110, AISON C4 HALVO<br>VDS GRANTEC TO-2</p>
    <div class="band band--blue">SPECIFICATION</div>
    <p class="spec">APX SL/CF, AVEA A3/B4<br>MINERAL OIL</p>
    <div class="seal" role="img" aria-label="Gold grade seal"></div>
    <div class="volume">4L</div>
    <div class="award award--gold" role="img" aria-label="Award badge"></div>
    <div class="award award--dark" role="img" aria-label="Reader award badge"></div>
    <div class="purity">100%<br>VIRGIN<span class="purity__big">OIL</span></div>
  </section>

</body>
</html>
```